Orlett Dental Care Small Tote Bag

Orlett Dental Care needs an advertisement design for a PressKite Small Tote Bag. See website "www.orlettdental.example." See uploaded files for small tote bag design template, color scheme, logos, and photo image of Dr. Orlett. Designer may crop photo as necessary.

Target Market(s)

Target market is Adults ages 35 to 80.

Industry/Entity Type

Dental

Font styles to use
Sans Serif

```html
<!DOCTYPE html>
<html lang="en">
<head>
<meta charset="utf-8">
<title>Orlett Dental Care – Small Tote Bag</title>
<link rel="stylesheet" href="https://fonts.googleapis.com/css2?family=Lato:wght@400;700;900&display=swap">
<style>
  :root {
    --canvas-bg: #f1efe9;
    --green-dark: #24493f;
    --green-mid: #4c8270;
    --green-soft: #6f9d8f;
    --taupe: #7d6b60;
    --rule: #9fb7ae;
    --band-top: #3b6b5e;
    --band-bottom: #234a3f;
    --white: #ffffff;
  }
  html, body {
    margin: 0;
    padding: 0;
    overflow: hidden;
  }
  .tote-print {
    position: relative;
    width: 1200px;
    height: 1000px;
    background: var(--canvas-bg);
    font-family: "Lato", sans-serif;
    overflow: hidden;
  }
  .brand-name {
    position: absolute;
    left: 143px;
    top: 340px;
    width: 887px;
    margin: 0;
    text-align: center;
    white-space: nowrap;
    font-family: "Lato", sans-serif;
    font-weight: 400;
    font-size: 96px;
    line-height: 120px;
    color: var(--green-dark);
  }
  .tagline {
    position: absolute;
    left: 204px;
    top: 568px;
    width: 246px;
    margin: 0;
    text-align: center;
    font-weight: 700;
    font-size: 27px;
    line-height: 40px;
  }
  .tagline .line-one, .tagline .line-three { color: var(--taupe); }
  .tagline .line-two { color: var(--green-mid); }
  .phone-icon {
    position: absolute;
    left: 468px;
    top: 558px;
    width: 74px;
    height: 132px;
  }
  .call-block {
    position: absolute;
    left: 563px;
    top: 556px;
    margin: 0;
    color: var(--green-dark);
    font-weight: 900;
  }
  .call-block .call-lead {
    display: block;
    font-size: 46px;
    line-height: 56px;
  }
  .call-block .call-number {
    display: block;
    font-size: 58px;
    line-height: 72px;
  }
  .divider {
    position: absolute;
    left: 204px;
    top: 714px;
    width: 763px;
    height: 2px;
    background: var(--rule);
  }
  .social {
    position: absolute;
    top: 736px;
    display: flex;
    align-items: center;
    gap: 12px;
    font-weight: 400;
    font-size: 40px;
    line-height: 44px;
    color: var(--green-dark);
  }
  .social-page { left: 190px; }
  .social-handle { left: 680px; }
  .social .dot {
    width: 34px;
    height: 34px;
    border-radius: 50%;
    background: var(--green-soft);
  }
  .web-band {
    position: absolute;
    left: 143px;
    top: 798px;
    width: 887px;
    height: 136px;
    background: linear-gradient(180deg, var(--band-top), var(--band-bottom));
    display: flex;
    align-items: center;
    justify-content: center;
    color: var(--white);
    font-size: 60px;
    font-weight: 400;
  }
  .web-band strong { font-weight: 900; }
</style>
</head>
<body>
<main class="tote-print">
  <h1 class="brand-name">Orlett Dental Care</h1>

  <p class="tagline">
    <span class="line-one">Life-Changing</span><br>
    <span class="line-two">Family Dental Care</span><br>
    <span class="line-three">In Fernhollow</span>
  </p>

  <svg class="phone-icon" viewBox="0 0 74 132" aria-hidden="true">
    <rect x="2" y="2" width="70" height="128" rx="10" fill="var(--green-mid)"/>
    <rect x="12" y="14" width="50" height="40" rx="3" fill="var(--canvas-bg)"/>
    <g fill="var(--canvas-bg)">
      <rect x="12" y="66" width="13" height="10" rx="2"/>
      <rect x="31" y="66" width="13" height="10" rx="2"/>
      <rect x="50" y="66" width="13" height="10" rx="2"/>
      <rect x="12" y="82" width="13" height="10" rx="2"/>
      <rect x="31" y="82" width="13" height="10" rx="2"/>
      <rect x="50" y="82" width="13" height="10" rx="2"/>
      <rect x="12" y="98" width="13" height="10" rx="2"/>
      <rect x="31" y="98" width="13" height="10" rx="2"/>
      <rect x="50" y="98" width="13" height="10" rx="2"/>
      <rect x="31" y="114" width="13" height="8" rx="2"/>
    </g>
  </svg>

  <p class="call-block">
    <span class="call-lead">Call Us Today!</span>
    <span class="call-number">(555) 014-2760</span>
  </p>

  <div class="divider"></div>

  <div class="social social-page"><span class="dot"></span><span>Orlett Dental Care</span></div>
  <div class="social social-handle"><span class="dot"></span><span>@OrlettDental</span></div>

  <div class="web-band">www.<strong>orlettdental</strong>.example</div>
</main>
</body>
</html>
```